Corrowin Sack operates across the US and Australasia providing calico bags to small business through to large enterprise across all verticals. Our bags are the most premium in the market place and our customer service is second to none. Our competitive advantage lays in our competitive pricing, superior quality and outstanding customer service.

Industry/Entity Type

Business

Contact Information for Business Card

Corrowin Sack
Marisol Quenby
Managing Director
marisol@corrowinsack.com
www.corrowinsack.com.au
Mobile:- 0471 896 305
Level 3, 284 Harwick Street
Melbourne Victoria Australia 3000

```html
<!DOCTYPE html>
<html lang="en">
<head>
<meta charset="utf-8">
<title>Corrowin Sack – Business Card</title>
<link rel="stylesheet" href="https://fonts.googleapis.com/css2?family=Tinos:wght@400;700&display=swap">
<style>
  :root {
    --page: #efece6;
    --linen: #ebe6dc;
    --linen-dark: #e1dbcf;
    --ink: #2b2b2b;
    --heading-grey: #8a8a88;
    --brand-green: #4f9a2c;
    --frame-green: #4b8a23;
    --accent-red: #c8102e;
    --photo-light: #e9ebe2;
    --photo-mid: #d9d5c8;
    --photo-warm: #b79f7e;
  }
  * { box-sizing: border-box; margin: 0; padding: 0; }
  html, body {
    width: 1003px; height: 1200px; overflow: hidden;
    background: var(--page);
    font-family: "Tinos", "Times New Roman", serif;
    color: var(--ink);
  }
  .card {
    position: absolute; left: 127px; width: 780px; height: 469px;
    background: linear-gradient(135deg, var(--linen), var(--linen-dark));
    box-shadow: 0 6px 16px rgba(0,0,0,0.18);
    overflow: hidden;
  }
  .card--front { top: 113px; }
  .card--back { top: 634px; }

  .brand-name {
    position: absolute; text-align: center;
    font-weight: 700; color: var(--brand-green);
    line-height: 1.05; letter-spacing: 0.5px;
  }
  .brand-mark {
    display: block; width: 18px; height: 18px; border-radius: 50%;
    background: var(--brand-green); margin: 0 auto 8px;
  }

  /* front */
  .front-panel { position: absolute; left: 0; top: 0; width: 317px; height: 100%; }
  .front-panel .brand-name { left: 0; width: 317px; top: 100px; font-size: 30px; }
  .product-title {
    position: absolute; left: 0; width: 317px; top: 282px;
    text-align: center; font-weight: 700; font-size: 54px; line-height: 66px;
    color: var(--heading-grey); letter-spacing: 2px;
    text-shadow: 1px 1px 0 #5c5c5a, -1px -1px 0 #f4f2ee;
  }
  .front-photo {
    position: absolute; left: 317px; top: 0; right: 0; bottom: 0;
    background: linear-gradient(180deg, var(--photo-light) 0%, var(--photo-mid) 70%, var(--photo-warm) 100%);
  }

  /* back */
  .card--back .brand-name { left: 100px; width: 200px; top: 42px; font-size: 28px; }
  .contact-name { position: absolute; left: 43px; top: 180px; font-size: 25px; font-weight: 700; }
  .contact-role { position: absolute; left: 43px; top: 208px; font-size: 25px; }
  .contact-list { position: absolute; left: 43px; top: 258px; list-style: none; font-size: 25px; }
  .contact-list li { display: flex; align-items: flex-start; margin-bottom: 9px; line-height: 29px; }
  .contact-list svg { width: 22px; height: 22px; margin: 4px 8px 0 0; flex: none; }
  .back-photo {
    position: absolute; left: 408px; top: 42px; width: 370px; height: 330px;
    border: 6px solid var(--frame-green);
    transform: rotate(-7deg);
    background: linear-gradient(160deg, #cfd3c6 0%, #e8e4d8 45%, #b89f80 100%);
  }
</style>
</head>
<body>
  <section class="card card--front">
    <div class="front-panel">
      <div class="brand-name"><span class="brand-mark"></span>Corrowin<br>Sack</div>
      <h1 class="product-title">CALICO<br>BAGS</h1>
    </div>
    <div class="front-photo" role="img" aria-label="Photo of plain calico drawstring bags in several sizes beside a wire basket"></div>
  </section>

  <section class="card card--back">
    <div class="brand-name"><span class="brand-mark"></span>Corrowin<br>Sack</div>
    <p class="contact-name">Marisol Quenby</p>
    <p class="contact-role">Managing Director</p>
    <ul class="contact-list">
      <li>
        <svg viewBox="0 0 22 22" aria-hidden="true"><rect x="5" y="2" width="12" height="18" rx="2" fill="none" stroke="var(--accent-red)" stroke-width="2"/><circle cx="11" cy="17" r="1.2" fill="var(--accent-red)"/></svg>
        0471 896 305
      </li>
      <li>
        <svg viewBox="0 0 22 22" aria-hidden="true"><rect x="2" y="5" width="18" height="12" fill="none" stroke="var(--accent-red)" stroke-width="2"/><path d="M2 5 L11 12 L20 5" fill="none" stroke="var(--accent-red)" stroke-width="2"/></svg>
        marisol@corrowinsack.com
      </li>
      <li>
        <svg viewBox="0 0 22 22" aria-hidden="true"><path d="M11 1 C6 1 3 5 3 9 C3 14 11 21 11 21 C11 21 19 14 19 9 C19 5 16 1 11 1 Z" fill="var(--accent-red)"/><circle cx="11" cy="9" r="3" fill="var(--linen)"/></svg>
        <span>Level 3, 284 Harwick Street<br>Melbourne Victoria Australia 3000</span>
      </li>
    </ul>
    <div class="back-photo" role="img" aria-label="Photo of a small calico gift bag with a printed greeting, beside a wire basket"></div>
  </section>
</body>
</html>
```